Business card design needed

The company name is Pellwick Architects. We are an architectural company based in Melbourne,Australia that has a mix of client base from health care, commercial office, aged care, multi-residential, single residential and retail. Design type is contemporary.

Suggest the base colours need to be black and white. Please leave an area on the back of the card available for handwritten notes.

Target Market(s)

Generally corporate, aged 30 to 65

Industry/Entity Type

Residential

Contact Information for Business Card

Pellwick Architects
Dane Pellwick
7 Horbury Street
Northvale VIC 3059
T (03) 9572 4016
M 0431 607 295
E dp@pellwickarc.com.au

Logo Text

PA

Logo styles of interest
Emblem Logo
Abstract Logo
Lettermark Logo
Requirements
Must have
• I am having trouble attaching a sketch so would really appreciate your effort to try the following brief.

Black and White (B&W)
Would like different card cutout profile. Logo Example, use the half circle curve of the G to form the left edge of the card with no margin. The A is to sit inside the G, connected to the G by its horizontal. The A has its cross bar and lower right leg removed. Card in black, text in white.

Back of card to be black text on white background with services provided.

Client Focused Service
Architecture and Design
Functional Planning
Town Planning
Feasability Studies
Contract Documentation
Contract Administration
Project Management

Simple elegant text, Ariel or similar
Nice to have
• Integrated logo and card cut-out.

Card base black on front, white on back
Should not have
• Too many colours
Fussy details

```html
<!DOCTYPE html>
<html lang="en">
<head>
<meta charset="utf-8">
<title>Pellwick Architects – Business Card</title>
<link rel="stylesheet" href="https://fonts.googleapis.com/css2?family=Arimo:wght@400;700&display=swap">
<style>
  :root {
    --ink: #000000;
    --paper: #ffffff;
    --mid-grey: #808080;
    --rule-grey: #9a9a9a;
    --bullet-grey: #6e6e6e;
  }
  * { margin: 0; padding: 0; box-sizing: border-box; }
  html, body {
    width: 1000px;
    height: 1200px;
    overflow: hidden;
    background: var(--paper);
    font-family: "Arimo", Arial, sans-serif;
  }
  .canvas { position: relative; width: 1000px; height: 1200px; }

  /* Front of card */
  .card-front {
    position: absolute;
    left: 85px; top: 35px;
    width: 870px; height: 520px;
    background: var(--ink);
    color: var(--paper);
  }
  .brand-mark {
    position: absolute;
    left: 60px; top: 150px;
    width: 340px;
    font-weight: 700;
    font-size: 190px;
    line-height: 1;
    letter-spacing: -4px;
    text-align: center;
    color: var(--paper);
  }
  .company-name {
    position: absolute;
    right: 37px; top: 122px;
    font-weight: 700;
    font-size: 38px;
    white-space: nowrap;
  }
  .person-name {
    position: absolute;
    right: 37px; top: 244px;
    font-weight: 700;
    font-size: 31px;
    white-space: nowrap;
  }
  .contact-list {
    position: absolute;
    right: 37px; top: 322px;
    list-style: none;
    text-align: right;
    font-size: 24px;
    line-height: 31px;
    white-space: nowrap;
  }

  /* Back of card */
  .card-back {
    position: absolute;
    left: 44px; top: 643px;
    width: 923px; height: 523px;
    background: var(--paper);
    border: 1px solid var(--rule-grey);
    color: var(--ink);
  }
  .services-heading {
    position: absolute;
    left: 320px; top: 105px;
    width: 602px; height: 34px;
    background: var(--ink);
    color: var(--paper);
    font-weight: 700;
    font-size: 30px;
    line-height: 34px;
    padding-left: 7px;
    white-space: nowrap;
  }
  .services-list {
    position: absolute;
    left: 395px; top: 151px;
    list-style: none;
    font-size: 33px;
    line-height: 39.5px;
    white-space: nowrap;
  }
  .services-list li { position: relative; padding-left: 56px; }
  .services-list li::before {
    content: "";
    position: absolute;
    left: 4px; top: 13px;
    width: 14px; height: 14px;
    border: 1.5px solid var(--bullet-grey);
    border-radius: 50%;
  }
  .footer-band {
    position: absolute;
    left: 0; bottom: 2px;
    width: 100%; height: 30px;
    display: flex;
  }
  .footer-band .band-dark { width: 461px; background: var(--ink); }
  .footer-band .band-grey { flex: 1; background: var(--mid-grey); }
</style>
</head>
<body>
<main class="canvas">
  <section class="card-front" aria-label="Front of card">
    <div class="brand-mark">PA</div>
    <h1 class="company-name">Pellwick Architects</h1>
    <h2 class="person-name">Dane Pellwick</h2>
    <ul class="contact-list">
      <li>7 Horbury Street</li>
      <li>Northvale VIC 3059</li>
      <li>T (03) 9572 4016</li>
      <li>M 0431 607 295</li>
      <li>E dp@pellwickarc.com.au</li>
    </ul>
  </section>

  <section class="card-back" aria-label="Back of card">
    <h2 class="services-heading">Client Focused Service</h2>
    <ul class="services-list">
      <li>Architecture and Design</li>
      <li>Functional Planning</li>
      <li>Town Planning</li>
      <li>Feasability Studies</li>
      <li>Contract Documentation</li>
      <li>Contract Administration</li>
      <li>Project Management</li>
    </ul>
    <div class="footer-band">
      <div class="band-dark"></div>
      <div class="band-grey"></div>
    </div>
  </section>
</main>
</body>
</html>
```